Property Management Company looking for a high-end business card, letterhead and envelope design.

We provide high-end / boutique property management for real estate investors or individuals looking for someone to manage their portfolio. we are looking for a cohesive high-end design for our business cards, letterhead and envelopes.

Target Market(s)

Real Estate Investors

Industry/Entity Type

Real Estate

Requirements
Must have
• business card, letterhead and envelope design - logo attached

```html
<!DOCTYPE html>
<html lang="en">
<head>
<meta charset="utf-8">
<title>Haleworth Stationery</title>
<link href="https://fonts.googleapis.com/css2?family=Montserrat:wght@500;600&family=Arimo:wght@400;700&display=swap" rel="stylesheet">
<style>
:root{
  --bg:#eef0f3;
  --paper:#e6e8ec;
  --envelope:#eceef1;
  --blue:#1f5590;
  --grey:#a1a5ab;
  --ink:#2b2e33;
  --label:#7d8085;
}
*{margin:0;padding:0;box-sizing:border-box}
html,body{width:1200px;height:900px;overflow:hidden;background:var(--bg)}
body{position:relative;font-family:Arimo,Arial,sans-serif;color:var(--ink)}
.label{position:absolute;transform:translateX(-50%);color:var(--label);font-size:14.5px;white-space:nowrap}
.label.small{font-size:7.5px}
.piece{position:absolute;background:var(--paper);box-shadow:0 6px 14px rgba(40,50,70,.16)}
.card{border-radius:6px;overflow:hidden}
.band{position:absolute;left:0;bottom:0;width:100%;display:block}
.logo{position:absolute;font-family:Montserrat,Arial,sans-serif;color:var(--blue);line-height:1}
.logo-name{display:block;font-weight:600;letter-spacing:.17em}
.logo-tag{display:block;font-weight:500;letter-spacing:.2em;margin-top:.35em}
.contact{position:absolute;display:flex;gap:10px;font-size:5px;line-height:1.45;color:var(--ink)}
.contact ul{list-style:none}
.contact li{display:flex;align-items:center;gap:3px}
.contact svg{width:1.3em;height:1.3em;fill:var(--blue);flex:none}
.contact .address{display:flex;gap:3px}
.contact .address svg{width:1.6em;height:1.8em}
.person-name{position:absolute;font-weight:700;letter-spacing:.03em}
.person-role{display:block;font-weight:400;letter-spacing:0;margin-top:2px;font-size:.78em}
</style>
</head>
<body>
<svg width="0" height="0" style="position:absolute" aria-hidden="true">
  <symbol id="i-phone" viewBox="0 0 10 10"><path d="M1 3.5C1 2 3 1.5 5 1.5S9 2 9 3.5L7.5 4.3 6.8 3.4H3.2L2.5 4.3zM2.5 5h5l1 3.5h-7z"/></symbol>
  <symbol id="i-mail" viewBox="0 0 10 10"><path d="M1 2.5h8v5H1zM1.6 3 5 5.6 8.4 3" stroke="#e6e8ec" stroke-width=".6"/></symbol>
  <symbol id="i-web" viewBox="0 0 10 10"><circle cx="5" cy="5" r="4"/><path d="M1 5h8M5 1c-2 2.2-2 5.8 0 8M5 1c2 2.2 2 5.8 0 8" stroke="#e6e8ec" stroke-width=".6" fill="none"/></symbol>
  <symbol id="i-pin" viewBox="0 0 10 12"><path d="M5 0a4 4 0 0 1 4 4c0 3-4 8-4 8S1 7 1 4a4 4 0 0 1 4-4zm0 2.3a1.7 1.7 0 1 0 0 3.4 1.7 1.7 0 0 0 0-3.4z"/></symbol>
</svg>

<!-- Letterhead -->
<span class="label" style="left:390px;top:40px">Letterhead</span>
<section class="piece letterhead" style="left:214px;top:76px;width:368px;height:521px">
  <div class="logo" style="left:21px;top:28px"><span class="logo-name" style="font-size:13.5px">HALEWORTH</span><span class="logo-tag" style="font-size:5.6px">PROPERTY MANAGEMENT</span></div>
  <div class="contact" style="left:229px;top:27px;font-size:4.3px">
    <ul>
      <li><svg><use href="#i-phone"/></svg>01632 960418</li>
      <li><svg><use href="#i-mail"/></svg>info@haleworth.com</li>
      <li><svg><use href="#i-web"/></svg>www.haleworth.com</li>
    </ul>
    <div class="address"><svg><use href="#i-pin"/></svg><p>Ridge House, Elmfield Park<br>Carrow Lane, Alnbury<br>Northshire, NE99 1ZZ</p></div>
  </div>
  <svg class="band" height="11" viewBox="0 0 368 11" preserveAspectRatio="none"><polygon points="0,0 176,0 186,11 0,11" fill="var(--blue)"/><polygon points="182,0 368,0 368,11 192,11" fill="var(--grey)"/></svg>
</section>

<!-- Complimentary slip -->
<span class="label" style="left:900px;top:200px">Complimentary Slip</span>
<section class="piece slip" style="left:658px;top:237px;width:483px;height:227px">
  <div class="logo" style="left:15px;top:24px"><span class="logo-name" style="font-size:13.5px">HALEWORTH</span><span class="logo-tag" style="font-size:5.6px">PROPERTY MANAGEMENT</span></div>
  <p class="person-name" style="left:15px;top:162px;font-size:8px">Marcus Holloway<span class="person-role">Managing Director</span></p>
  <div class="contact" style="left:15px;top:187px;font-size:5px">
    <ul>
      <li><svg><use href="#i-phone"/></svg>01632 960418</li>
      <li><svg><use href="#i-mail"/></svg>info@haleworth.com</li>
      <li><svg><use href="#i-web"/></svg>www.haleworth.com</li>
    </ul>
    <div class="address"><svg><use href="#i-pin"/></svg><p>Ridge House, Elmfield Park<br>Carrow Lane, Alnbury<br>Northshire, NE99 1ZZ</p></div>
  </div>
  <svg class="band" height="7" viewBox="0 0 483 7" preserveAspectRatio="none"><polygon points="0,0 238,0 245,7 0,7" fill="var(--blue)"/><polygon points="242,0 483,0 483,7 249,7" fill="var(--grey)"/></svg>
</section>

<!-- Business card -->
<span class="label" style="left:166px;top:606px">Business Card</span>
<span class="label small" style="left:166px;top:628px">Back</span>
<section class="piece card card-back" style="left:79px;top:638px;width:174px;height:97px">
  <div class="logo" style="left:32px;top:39px"><span class="logo-name" style="font-size:11.5px">HALEWORTH</span><span class="logo-tag" style="font-size:4.9px">PROPERTY MANAGEMENT</span></div>
</section>
<span class="label small" style="left:166px;top:750px">Front</span>
<section class="piece card card-front" style="left:77px;top:759px;width:177px;height:98px;border-radius:6px 6px 0 0">
  <div class="logo" style="left:13px;top:20px"><span class="logo-name" style="font-size:7.6px">HALEWORTH</span><span class="logo-tag" style="font-size:3.2px">PROPERTY MANAGEMENT</span></div>
  <p class="person-name" style="left:97px;top:20px;font-size:5.6px">Marcus Holloway<span class="person-role">Managing Director</span></p>
  <div class="contact" style="left:13px;top:66px;font-size:3.3px">
    <div class="address"><svg><use href="#i-pin"/></svg><p>Ridge House, Elmfield Park<br>Carrow Lane, Alnbury<br>Northshire, NE99 1ZZ</p></div>
  </div>
  <div class="contact" style="left:97px;top:66px;font-size:3.3px">
    <ul>
      <li><svg><use href="#i-phone"/></svg>01632 960418</li>
      <li><svg><use href="#i-mail"/></svg>info@haleworth.com</li>
      <li><svg><use href="#i-web"/></svg>www.haleworth.com</li>
    </ul>
  </div>
  <svg class="band" height="7" viewBox="0 0 177 7" preserveAspectRatio="none"><polygon points="0,0 86,0 92,7 0,7" fill="var(--blue)"/><polygon points="89,0 177,0 177,7 95,7" fill="var(--grey)"/></svg>
</section>

<!-- Envelope front -->
<span class="label" style="left:495px;top:634px">Envelope Front</span>
<section class="piece envelope-front" style="left:290px;top:654px;width:412px;height:197px">
  <div class="logo" style="left:20px;top:28px"><span class="logo-name" style="font-size:13.5px">HALEWORTH</span><span class="logo-tag" style="font-size:5.6px">PROPERTY MANAGEMENT</span></div>
  <div class="contact" style="left:20px;top:157px;font-size:5px">
    <ul>
      <li><svg><use href="#i-phone"/></svg>01632 960418</li>
      <li><svg><use href="#i-mail"/></svg>info@haleworth.com</li>
      <li><svg><use href="#i-web"/></svg>www.haleworth.com</li>
    </ul>
    <div class="address"><svg><use href="#i-pin"/></svg><p>Ridge House, Elmfield Park<br>Carrow Lane, Alnbury<br>Northshire, NE99 1ZZ</p></div>
  </div>
  <svg class="band" height="7" viewBox="0 0 412 7" preserveAspectRatio="none"><polygon points="0,0 201,0 208,7 0,7" fill="var(--blue)"/><polygon points="205,0 412,0 412,7 212,7" fill="var(--grey)"/></svg>
</section>

<!-- Envelope back -->
<span class="label" style="left:945px;top:634px">Envelope Back</span>
<section class="envelope-back" style="position:absolute;left:736px;top:654px;width:416px;height:197px">
  <svg width="416" height="197" viewBox="0 0 416 197">
    <rect x="5" y="8" width="405" height="189" fill="var(--envelope)" style="filter:drop-shadow(0 5px 8px rgba(40,50,70,.15))"/>
    <polygon points="0,0 169,0 237,69 14,71" fill="var(--blue)"/>
    <polygon points="176,0 415,0 409,67 245,69" fill="var(--grey)"/>
  </svg>
</section>
</body>
</html>
```